Business Cards for Tandrix Office
Simplifying your policy needs
Bright & Fun-filled
Gordon Lavelle
CEO
8 Carrow Lane Unit #342 Marblehead, MA 01862
glavelle@tandrixoffice.net
www.tandrixoffice.net
Please view our site at www.tandrixoffice.net to understand what we are doing. we have created on online solution to help Credit Union manage and distribute their policies and procedures. Looking at rounded corners and 14pt stock paper
The URL of the site is VERY important since everything is online

```html
<!DOCTYPE html>
<html lang="en">
<head>
<meta charset="utf-8">
<title>Tandrix Office — Business Cards</title>
<link href="https://fonts.googleapis.com/css2?family=Open+Sans:wght@400;600;700&display=swap" rel="stylesheet">
<style>
  :root {
    --backdrop: #3b2219;
    --card-blue: #2a86d6;
    --card-blue-light: #5ab3f0;
    --card-blue-deep: #1c6cb8;
    --accent-green: #5db030;
    --paper: #ffffff;
    --ink-blue: #1f7fd0;
  }
  * { margin: 0; padding: 0; box-sizing: border-box; }
  html, body {
    width: 1200px; height: 897px; overflow: hidden;
    background: var(--backdrop);
    font-family: "Open Sans", Arial, sans-serif;
  }
  .stage {
    width: 1200px; height: 897px;
    display: flex; align-items: center; justify-content: center; gap: 40px;
  }
  .card {
    position: relative;
    width: 540px; height: 310px;
    border-radius: 22px; overflow: hidden;
    box-shadow: 0 10px 24px rgba(0,0,0,.45);
  }
  .card-art { position: absolute; inset: 0; }
  .brand {
    position: absolute; left: 28px; top: 128px;
    display: flex; align-items: center; gap: 10px;
  }
  .brand-dot {
    width: 34px; height: 34px; border-radius: 50%;
    background: var(--accent-green);
    flex: none;
  }
  .brand-name {
    font-size: 23px; font-weight: 700; color: var(--ink-blue);
    line-height: 1.05;
  }
  .contact {
    position: absolute; right: 30px; top: 34px;
    text-align: right; color: var(--paper);
    font-size: 12px; line-height: 1.55;
  }
  .contact .name { font-size: 17px; font-weight: 700; line-height: 1.2; }
  .contact .title { font-size: 12px; margin-bottom: 12px; }
  .contact .block { margin-bottom: 10px; }
  .contact .web { font-size: 15px; font-weight: 700; }
  .card-back {
    background: radial-gradient(circle at 50% 42%, var(--card-blue-light) 0%, var(--card-blue) 45%, var(--card-blue-deep) 100%);
  }
  .back-mark {
    position: absolute; left: 50%; top: 92px;
    width: 70px; height: 70px; margin-left: -35px;
    border-radius: 50%; background: var(--paper);
  }
  .back-url {
    position: absolute; left: 0; right: 0; top: 186px;
    text-align: center; color: var(--paper);
    font-size: 22px; font-weight: 600;
  }
</style>
</head>
<body>
<main class="stage">
  <section class="card card-front">
    <svg class="card-art" viewBox="0 0 540 310" width="540" height="310" aria-hidden="true">
      <rect width="540" height="310" fill="var(--card-blue)"/>
      <path d="M0,0 H272 C206,84 188,214 226,310 H0 Z" fill="var(--accent-green)"/>
      <path d="M0,0 H256 C192,84 174,214 212,310 H0 Z" fill="var(--paper)"/>
    </svg>
    <div class="brand">
      <span class="brand-dot"></span>
      <span class="brand-name">Tandrix<br>Office</span>
    </div>
    <div class="contact">
      <div class="name">Gordon Lavelle</div>
      <div class="title">CEO</div>
      <div class="block">8 Carrow Lane Unit #342<br>Marblehead, MA 01862</div>
      <div class="block">Tel: 781.555.0142<br>Fax: 781.555.0143<br>Cell: 781.555.0144</div>
      <div>glavelle@tandrixoffice.net</div>
      <div class="web">www.tandrixoffice.net</div>
    </div>
  </section>

  <section class="card card-back">
    <div class="back-mark"></div>
    <div class="back-url">www.tandrixoffice.net</div>
  </section>
</main>
</body>
</html>
```